Double-sided half page marketing handout for professional association conference

We need a collatoral piece that will go into conference attendees' registration packets. Handout will be double-sided, half-letter-sized page. Working print area is 8.1" by 5.3" for each side. Can be laid out either vertically or horizontally.

One side of the piece will be focused on my firm's contact information and broad scope of services:

Contact Information:
Velmont Partners LLC
Local Government Consultants
415-630-2918
www.velmontpartners.example
info@velmontpartners.example

Services:
Bond Rating Assessments
Economic Development Consulting
Executive Dashboards
Public Policy Analysis
Governance Training & Support
Strategic Planning & Performance Management

The other side of the piece will focus on the Bond Rating Assessments (see http://www.velmontpartners.example/Pages/Bond-Rating-Assessments.aspx and attachments for more detail). This side should contain the text:

"Considering issuing debt? Bond ratings make a difference. Did you know that on an average $20 million GO debt issuance a one rating-level difference can easily equate to over $350,000 in interest cost-savings under normal market conditions?

The ratings agencies use a combined quantitative and qualitative approach to arrive at your bond rating. Our Bond Ratings Assessment shows you precisely what the agencies are looking at, provides advice as to how to frame the conversation during ratings calls, and identifies both strategic opportunities to provide upgrade pressure and specific threats that may lead to a downgrade. Call or email us to find out more or to get an example assessment."

Go to www.velmontpartners.example and see attached files for logo and a recent winning ArtHive 1/4 page advertisement for style guidance.

Target Market(s)

Highly-educated, conservative local government executives.

Industry/Entity Type

Marketing

Font styles to use
Sans Serif

Colors
3277b5
85acd3
ffffff

Requirements
Must have
• Our logo, our contact information, basic information stated in Project Description. Feel free to modify language to make more clear or understandable.
Nice to have
• We rather not just a text piece - bringing in some graphical elements would be very nice.

```html
<!DOCTYPE html>
<html lang="en">
<head>
<meta charset="utf-8">
<title>Velmont Partners LLC – Conference Handout</title>
<link rel="stylesheet" href="https://fonts.googleapis.com/css2?family=Roboto+Condensed:ital,wght@0,400;0,700;1,700&display=swap">
<style>
  :root {
    --brand-blue: #3277b5;
    --brand-sky: #85acd3;
    --brand-white: #ffffff;
    --ink: #1d1d1d;
    --pale: rgba(236, 241, 248, 0.86);
    --divider: #000000;
  }
  * { box-sizing: border-box; margin: 0; padding: 0; }
  html, body { width: 1200px; height: 917px; overflow: hidden; background: var(--brand-white); }
  body { position: relative; font-family: "Roboto Condensed", "Arial Narrow", sans-serif; color: var(--ink); }

  .divider { position: absolute; left: 580px; top: 0; width: 32px; height: 917px; background: var(--divider); }

  .side { position: absolute; top: 23px; width: 549px; height: 872px; overflow: hidden; background: #dfe7f1; }
  .side--front { left: 23px; }
  .side--back { left: 630px; }

  .photo { position: absolute; left: 0; top: 0; width: 100%; height: 470px; }
  .side--front .photo { background: linear-gradient(115deg, #4d5560 0%, #9aa3ad 35%, #d5d9de 60%, #6f7b88 100%); }
  .side--back .photo { background: linear-gradient(160deg, #f4f6fa 0%, #d9e1ec 45%, #aebccf 100%); }
  .photo-fade { position: absolute; left: 0; top: 300px; width: 100%; height: 200px; background: linear-gradient(to bottom, rgba(223,231,241,0), #dfe7f1); }

  .column { position: absolute; top: 0; bottom: 86px; background: var(--pale); border-left: 4px solid var(--brand-blue); }
  .side--front .column { left: 76px; width: 404px; border-right: 4px solid var(--brand-blue); }
  .side--back .column { left: 44px; width: 458px; border-right: 4px solid var(--brand-blue); background: rgba(240, 244, 250, 0.7); }

  .circle { position: absolute; }

  .title-band { position: absolute; left: 0; top: 34px; width: 100%; height: 53px; background: var(--brand-blue); color: var(--brand-white); font-weight: 700; font-size: 37px; line-height: 53px; padding-left: 22px; letter-spacing: -0.2px; }

  .body-copy { position: absolute; color: var(--ink); }
  .side--front .body-copy { left: 99px; top: 112px; width: 340px; font-size: 19.5px; line-height: 28.5px; }
  .side--front .body-copy p + p { margin-top: 7px; }
  .circle-wrap { float: right; width: 340px; height: 720px; shape-outside: circle(288px at 491px 530px); shape-margin: 16px; }
  .side--back .body-copy { left: 68px; top: 38px; width: 375px; font-size: 20px; line-height: 35.3px; }
  .body-copy strong { font-weight: 700; }

  .services { position: absolute; left: 70px; top: 340px; list-style: none; font-size: 20px; font-weight: 700; font-style: italic; line-height: 28px; }
  .services li { position: relative; padding-left: 19px; margin-bottom: 8px; width: 340px; }
  .services li.wrap-short { width: 230px; }
  .services li.wrap-narrow { width: 190px; }
  .services li::before { content: ""; position: absolute; left: 0; top: 8px; width: 7px; height: 13px; background: var(--brand-blue); border-radius: 0 7px 7px 0; }

  .cta { position: absolute; width: 200px; text-align: center; color: var(--brand-blue); font-weight: 700; font-size: 16.5px; line-height: 23px; }
  .side--front .cta { left: 94px; top: 656px; }
  .side--back .cta { left: 70px; top: 680px; }

  .brand { position: absolute; width: 200px; text-align: center; color: var(--brand-white); }
  .side--front .brand { left: 348px; top: 606px; }
  .side--back .brand { left: 340px; top: 596px; }
  .brand-name { font-size: 29px; font-weight: 700; line-height: 31px; color: var(--brand-white); }
  .brand-tag { margin-top: 12px; font-size: 16.5px; line-height: 23px; font-weight: 400; }

  .contact-band { position: absolute; left: 0; bottom: 16px; width: 100%; height: 70px; background: var(--brand-sky); text-align: center; font-size: 20px; line-height: 27px; padding-top: 9px; color: var(--ink); }
  .contact-band .row { display: flex; justify-content: center; align-items: center; gap: 14px; }
  .contact-band .item { display: inline-flex; align-items: center; gap: 6px; }
  .base-strip { position: absolute; left: 0; bottom: 0; width: 100%; height: 16px; background: var(--brand-blue); }
</style>
</head>
<body>
  <div class="divider"></div>

  <section class="side side--front">
    <div class="photo" role="img" aria-label="Financial documents and market figures in grey and blue tones"></div>
    <div class="photo-fade"></div>
    <div class="column"></div>
    <svg class="circle" style="left:300px;top:380px" width="249" height="406" viewBox="0 0 249 406" aria-hidden="true">
      <circle cx="290" cy="262" r="288" fill="#8fb2d8"/>
      <circle cx="290" cy="262" r="276" fill="#3277b5"/>
    </svg>
    <h1 class="title-band">Bond ratings make a difference.</h1>
    <div class="body-copy">
      <div class="circle-wrap" aria-hidden="true"></div>
      <p>Did you know that on an average $20 million GO debt issuance a one rating-level difference can easily equate to over $350,000 in interest cost-savings under normal market conditions?</p>
      <p>The ratings agencies use a combined quantitative and qualitative approach to arrive at your bond rating. <strong>Our Bond Ratings Assessment</strong> shows you <strong>precisely</strong> what the agencies are looking at, provides <strong>advice</strong> as to how to frame the conversation during ratings calls, and <strong>identifies</strong> both strategic <strong>opportunities</strong> to provide upgrade pressure and specific threats that may lead to a downgrade.</p>
    </div>
    <p class="cta">Call or email us to find out more or to get an example assessment.</p>
    <div class="brand">
      <div class="brand-name">Velmont Partners LLC</div>
      <div class="brand-tag">Local Government<br>Consultants</div>
    </div>
    <div class="contact-band">
      <div class="row">
        <span class="item"><svg width="24" height="16" viewBox="0 0 24 16" aria-hidden="true"><path d="M2 6 Q12 -2 22 6 L19 8 L16 5 H8 L5 8 Z" fill="#1d1d1d"/><rect x="5" y="8" width="14" height="7" rx="1" fill="#1d1d1d"/></svg>415-630-2918</span>
        <span class="item"><svg width="20" height="15" viewBox="0 0 20 15" aria-hidden="true"><rect x="1" y="1" width="18" height="13" fill="none" stroke="#1d1d1d" stroke-width="1.4"/><path d="M1 1 L10 8 L19 1" fill="none" stroke="#1d1d1d" stroke-width="1.4"/></svg>info@velmontpartners.example</span>
      </div>
      <div>Visit us at www.velmontpartners.example to learn more.</div>
    </div>
    <div class="base-strip"></div>
  </section>

  <section class="side side--back">
    <div class="photo" role="img" aria-label="Hand with pen beside a calculator keypad in soft blue light"></div>
    <div class="photo-fade"></div>
    <div class="column"></div>
    <svg class="circle" style="left:300px;top:400px" width="249" height="386" viewBox="0 0 249 386" aria-hidden="true">
      <circle cx="290" cy="242" r="262" fill="#8fb2d8"/>
      <circle cx="290" cy="242" r="250" fill="#3277b5"/>
    </svg>
    <p class="body-copy">&nbsp;All of the ratings agencies use a combination of quantitative and qualitative analysis to determine your ratings. We have worked with the ratings agencies to fully understand what their analysts are looking for and have developed a methodology to give you the insight needed to put your community’s best foot forward.</p>
    <ul class="services">
      <li>Bond Rating Assessments</li>
      <li>Economic Development Consulting</li>
      <li>Executive Dashboards</li>
      <li>Public Policy Analysis</li>
      <li class="wrap-short">Governance Training &amp; Support</li>
      <li class="wrap-narrow">Strategic Planning &amp; Performance Management</li>
    </ul>
    <p class="cta">Call or email us to find out more or to get an example assessment.</p>
    <div class="brand">
      <div class="brand-name">Velmont Partners LLC</div>
      <div class="brand-tag">Local Government<br>Consultants</div>
    </div>
    <div class="contact-band">
      <div class="row">
        <span class="item"><svg width="24" height="16" viewBox="0 0 24 16" aria-hidden="true"><path d="M2 6 Q12 -2 22 6 L19 8 L16 5 H8 L5 8 Z" fill="#1d1d1d"/><rect x="5" y="8" width="14" height="7" rx="1" fill="#1d1d1d"/></svg>415-630-2918</span>
        <span class="item"><svg width="20" height="15" viewBox="0 0 20 15" aria-hidden="true"><rect x="1" y="1" width="18" height="13" fill="none" stroke="#1d1d1d" stroke-width="1.4"/><path d="M1 1 L10 8 L19 1" fill="none" stroke="#1d1d1d" stroke-width="1.4"/></svg>info@velmontpartners.example</span>
      </div>
      <div>Visit us at www.velmontpartners.example to learn more.</div>
    </div>
    <div class="base-strip"></div>
  </section>
</body>
</html>
```